Business card and stationary for Intellectual Property Consultant & Law Firm
Harborline Claims Omniworks
Business card and stationary for Intellectual Property Consultant & Law Firm - Law
Creative Brief
Simple
Dorin Makalesu
President Director
Kelor Business Center 11th Floor Jl. Raya Wibisana Kav.37-38 Jakarta Pusat 10485, Indonesia
office@harborlineclaims.example
www.harborlineclaims.example
Member: OQRU, EKLM, UVBO, WDGF
Please add Intellectual Property Rights Consultant & Law Firm for letterhead additional of our email : hbl42@harborlineclaims.example; marks@harborlineclaims.example
please add Branch office : Surabaya (+6231) 480 3926 Medan (+6261) 819 4057 Solo (+62271) 634 918
trelvorin trelvorin
Dear All, Please provide me the stationary : letterhead, envelope, cds, ballpoint, ruler, stamps, usb sticks etc
dunmoral dunmoral
Please upload Ai or eps file of your logo thankyou
Please add : Intellectual Property Rights Consultant & Law Firm in envelope and letter head.

```html
<!DOCTYPE html>
<html lang="en">
<head>
<meta charset="utf-8">
<title>Harborline Claims Omniworks – Business Card</title>
<link rel="stylesheet" href="https://fonts.googleapis.com/css2?family=Montserrat:wght@400;500;600&display=swap">
<style>
  :root {
    --stage: #4b4b4b;
    --card-white: #f7f7f7;
    --card-silver: #dcdcdc;
    --card-grey: #707070;
    --card-grey-dark: #5e5e5e;
    --accent: #f2a31b;
    --accent-deep: #d98a0c;
    --ink: #5a5a5a;
    --ink-light: #ffffff;
  }
  * { margin: 0; padding: 0; box-sizing: border-box; }
  html, body { width: 1200px; height: 895px; overflow: hidden; }
  body {
    background: var(--stage);
    font-family: "Montserrat", Arial, sans-serif;
    position: relative;
  }
  .card {
    position: absolute;
    width: 540px;
    height: 310px;
    top: 292px;
    border-radius: 3px;
    overflow: hidden;
    box-shadow: 0 10px 24px rgba(0,0,0,.35);
  }
  .card-front { left: 40px; }
  .card-back { left: 620px; }
  .card-art { position: absolute; inset: 0; width: 100%; height: 100%; }

  .brand {
    position: absolute;
    left: 34px;
    top: 118px;
    color: var(--ink);
    font-weight: 500;
  }
  .brand-name { font-size: 30px; line-height: 32px; letter-spacing: -0.5px; }
  .brand-sub { font-size: 10px; letter-spacing: 4px; margin-top: 4px; }

  .holder {
    position: absolute;
    right: 26px;
    top: 22px;
    text-align: right;
    color: var(--ink-light);
  }
  .holder-name { font-size: 14px; font-weight: 500; letter-spacing: 1px; }
  .holder-role { font-size: 10px; margin-top: 3px; }

  .address {
    position: absolute;
    right: 26px;
    top: 84px;
    text-align: right;
    color: var(--ink-light);
    font-size: 10px;
    line-height: 14px;
  }

  .contacts {
    position: absolute;
    right: 22px;
    top: 130px;
    list-style: none;
    color: var(--ink-light);
    font-size: 8.5px;
  }
  .contacts li {
    display: flex;
    justify-content: flex-end;
    align-items: center;
    gap: 6px;
    height: 15px;
  }
  .contacts svg { width: 9px; height: 9px; fill: var(--ink-light); }

  .web {
    position: absolute;
    left: 0; right: 0;
    bottom: 20px;
    text-align: center;
    color: var(--ink);
    font-size: 15px;
    font-weight: 500;
    letter-spacing: 5px;
  }
</style>
</head>
<body>

<section class="card card-front" aria-label="Business card front">
  <svg class="card-art" viewBox="0 0 540 310" preserveAspectRatio="none">
    <defs>
      <linearGradient id="frontWhite" x1="0" y1="0" x2="1" y2="1">
        <stop offset="0" stop-color="#ffffff"/>
        <stop offset="1" stop-color="#e6e6e6"/>
      </linearGradient>
    </defs>
    <rect width="540" height="310" fill="url(#frontWhite)"/>
    <path d="M352,0 C262,70 262,240 342,310 L540,310 L540,0 Z" fill="var(--card-grey)"/>
    <path d="M352,0 C262,70 262,240 342,310" fill="none" stroke="var(--accent)" stroke-width="7"/>
  </svg>
  <div class="brand">
    <div class="brand-name">Harborline<br>Claims</div>
    <div class="brand-sub">OMNIWORKS</div>
  </div>
</section>

<section class="card card-back" aria-label="Business card back">
  <svg class="card-art" viewBox="0 0 540 310" preserveAspectRatio="none">
    <defs>
      <linearGradient id="backGrey" x1="0" y1="0" x2="0" y2="1">
        <stop offset="0" stop-color="var(--card-grey)"/>
        <stop offset="1" stop-color="var(--card-grey-dark)"/>
      </linearGradient>
      <linearGradient id="backSilver" x1="0" y1="0" x2="1" y2="1">
        <stop offset="0" stop-color="#ffffff"/>
        <stop offset="1" stop-color="var(--card-silver)"/>
      </linearGradient>
    </defs>
    <rect width="540" height="310" fill="url(#backGrey)"/>
    <path d="M0,262 C150,214 370,212 540,252 L540,310 L0,310 Z" fill="var(--accent)"/>
    <path d="M0,271 C150,225 370,223 540,261 L540,310 L0,310 Z" fill="url(#backSilver)"/>
  </svg>

  <div class="holder">
    <div class="holder-name">TOMAS REYVALD</div>
    <div class="holder-role">Managing Director</div>
  </div>

  <div class="address">041 12th floor, Quay Lantern<br>Road KPR</div>

  <ul class="contacts">
    <li>014 275 3860
      <svg viewBox="0 0 10 10"><path d="M2,0.5 L3.6,2.8 L2.7,3.8 C3.3,5 4.9,6.7 6.2,7.3 L7.2,6.4 L9.5,8 L8.3,9.6 C4.8,9.4 0.6,5.2 0.4,1.7 Z"/></svg>
    </li>
    <li>014 275 3860
      <svg viewBox="0 0 10 10"><path d="M2.5,0 H7.5 V10 H2.5 Z M3.3,1 V8 H6.7 V1 Z M4.5,8.6 H5.5 V9.4 H4.5 Z" fill-rule="evenodd"/></svg>
    </li>
    <li>014 275 3860
      <svg viewBox="0 0 10 10"><path d="M2.5,0 H7.5 V3 H2.5 Z M0.5,3.5 H9.5 V7.5 H8 V6 H2 V7.5 H0.5 Z M2.8,6.6 H7.2 V10 H2.8 Z"/></svg>
    </li>
    <li>yourname@mail.example
      <svg viewBox="0 0 10 10"><path d="M0.5,2 H9.5 V8 H0.5 Z M1.2,2.6 L5,5.4 L8.8,2.6" fill-rule="evenodd"/></svg>
    </li>
    <li>www.yoursitename.example
      <svg viewBox="0 0 10 10"><circle cx="5" cy="5" r="4.3" fill="none" stroke="#fff" stroke-width="1"/><path d="M0.8,5 H9.2 M5,0.7 C2.6,3 2.6,7 5,9.3 M5,0.7 C7.4,3 7.4,7 5,9.3" fill="none" stroke="#fff" stroke-width="0.8"/></svg>
    </li>
  </ul>

  <div class="web">www.yoursitename.example</div>
</section>

</body>
</html>
```